International sports company needs packaging design for color box

We need this box for our yoga mats which we will sell online. This mat is very high quality and 100% environmentally friendly. The yoga mat comes in a stylish yoga bag that will be in the box.

Yoga enthusiasts, athletes, gymnasts, actually all people who do sporting activities and value environmental friendliness will be the contact group

The logo should be visible in any case. The creator is free to choose whether to use only the complete logo or the complete logo with the emblem. In terms of style, it should be reminiscent of a packaging box from Zorvik's Valmox. Be as timeless, modern and elegant as possible. If an environmentally friendly detail can be added, this would certainly be a plus. Color should be black / white / gray.

Target Market(s)

Germany

Requirements
Must have
• Size for the color box should be 13x13x61.5 cm.

```html
<!DOCTYPE html>
<html lang="en">
<head>
<meta charset="utf-8">
<title>ORYNTH Yoga Mat Box</title>
<link rel="stylesheet" href="https://fonts.googleapis.com/css2?family=Montserrat:wght@400;700&family=Roboto+Condensed:wght@300;400;700&display=swap">
<style>
  :root {
    --backdrop: #c9d0d1;
    --box-black: #111111;
    --box-side: #0b0b0b;
    --ink-white: #f2f2f2;
    --ink-grey: #cfcfcf;
    --fold: #2a2a2a;
  }
  * { margin: 0; padding: 0; box-sizing: border-box; }
  html, body {
    width: 1200px;
    height: 789px;
    overflow: hidden;
    background: var(--backdrop);
    font-family: "Montserrat", sans-serif;
  }
  .canvas {
    position: relative;
    width: 1200px;
    height: 789px;
  }
  .box-lid {
    position: absolute;
    left: 170px;
    top: 110px;
    width: 860px;
    height: 400px;
    background: var(--box-black);
  }
  .lid-brand {
    position: absolute;
    left: 0;
    right: 0;
    top: 160px;
    text-align: center;
    color: var(--ink-white);
    font-weight: 700;
    font-size: 64px;
    line-height: 1;
    letter-spacing: 12px;
  }
  .lid-quality {
    position: absolute;
    right: 40px;
    top: 50%;
    transform: translateY(-50%) rotate(-90deg);
    transform-origin: center;
    color: var(--ink-white);
    font-family: "Roboto Condensed", sans-serif;
    font-weight: 400;
    font-size: 17px;
    line-height: 1.1;
    text-align: center;
    letter-spacing: 1px;
  }
  .box-side {
    position: absolute;
    left: 170px;
    top: 512px;
    width: 860px;
    height: 170px;
    background: var(--box-side);
    border-top: 2px solid var(--fold);
    display: flex;
    align-items: center;
    padding: 0 60px;
  }
  .eco-badge {
    display: flex;
    flex-direction: column;
    color: var(--ink-white);
    font-family: "Roboto Condensed", sans-serif;
    line-height: 1;
  }
  .eco-percent {
    display: flex;
    align-items: center;
    gap: 6px;
    font-weight: 700;
    font-size: 26px;
  }
  .eco-percent svg { width: 18px; height: 18px; }
  .eco-line {
    font-weight: 300;
    font-size: 17px;
    margin-top: 4px;
  }
  .eco-word {
    font-weight: 400;
    font-size: 28px;
    margin-top: 2px;
  }
  .side-brand {
    margin-left: auto;
    margin-right: 130px;
    color: var(--ink-grey);
    font-weight: 700;
    font-size: 38px;
    line-height: 1;
    letter-spacing: 10px;
  }
</style>
</head>
<body>
  <main class="canvas">
    <section class="box-lid">
      <div class="lid-brand">ORYNTH</div>
      <div class="lid-quality">PREMIUM<br>QUALITY</div>
    </section>
    <section class="box-side">
      <div class="eco-badge">
        <div class="eco-percent">
          <svg viewBox="0 0 20 20" aria-hidden="true">
            <path d="M3 17 C3 7 9 3 18 3 C18 12 13 17 3 17 Z" fill="var(--ink-white)"/>
            <path d="M4 16 L14 7" stroke="var(--box-side)" stroke-width="1.2"/>
          </svg>
          100%
          <svg viewBox="0 0 20 20" aria-hidden="true">
            <path d="M3 17 C3 7 9 3 18 3 C18 12 13 17 3 17 Z" fill="var(--ink-white)"/>
            <path d="M4 16 L14 7" stroke="var(--box-side)" stroke-width="1.2"/>
          </svg>
        </div>
        <div class="eco-line">Environmentally</div>
        <div class="eco-word">Friendly</div>
      </div>
      <div class="side-brand">ORYNTH</div>
    </section>
  </main>
</body>
</html>
```